7 ¾ long by 5 inches high print ad

I have a 1/2 page ad for a print magazine I need to be designed. Uploaded is the previous year design. We want something to be more aligned with our new website look/feel and new messaging from website.

I have provided some photos, the logo, color codes and a recent banner ad sample for copy.

Target Market(s)

Developers

Font styles to use
Sans Serif

Requirements
Must have
• Clear headline, sub headline, and value statement
• Services to highlight, Tilt-Up Construction,
• Website, phone, social icons, Fanpage, Posts, and Network
Nice to have
• https://marrowcrestbuilding.com/
• Some of the logos in the clients who trust us section

```html
<!DOCTYPE html>
<html lang="en">
<head>
<meta charset="utf-8">
<title>Marrowcrest Construction – Print Ad</title>
<link href="https://fonts.googleapis.com/css2?family=Arimo:wght@400;700&display=swap" rel="stylesheet">
<style>
  :root {
    --navy: #16213f;
    --orange: #d07f00;
    --slate: #55595e;
    --mist: #c2c3c4;
    --client-grey: #878c8f;
    --white: #ffffff;
    --ink: #16213f;
  }
  * { box-sizing: border-box; margin: 0; padding: 0; }
  html, body { width: 1200px; height: 775px; overflow: hidden; background: #fff; }
  body { font-family: "Arimo", Arial, sans-serif; }
  .ad { position: relative; width: 1200px; height: 775px; overflow: hidden; background: var(--white); }

  .top-band { position: absolute; left: 0; top: 0; width: 1200px; height: 31px; background: var(--navy); }

  .brand { position: absolute; left: 447px; top: 31px; height: 122px; display: flex; align-items: center; gap: 20px; }
  .brand-mark { width: 52px; height: 84px; background: var(--orange); }
  .brand-name { color: var(--orange); line-height: 1; }
  .brand-name .main { display: block; font-size: 38px; font-weight: 700; }
  .brand-name .sub { display: block; font-size: 21px; font-weight: 400; margin-top: 2px; padding-left: 4px; }

  .hero { position: absolute; left: 0; top: 153px; width: 1200px; height: 431px;
    background: linear-gradient(180deg, #7fa3c4 0%, #a9bdd0 30%, #d8c3c9 48%, #c9a7ae 56%, #4a4f55 62%, #3d4247 100%); }

  .headline { position: absolute; left: 41px; top: 181px; color: var(--ink); }
  .headline .lead { font-size: 18.5px; font-weight: 700; }
  .headline .title { font-size: 27.5px; font-weight: 700; color: var(--orange); margin-top: 3px; }
  .headline .value { font-size: 16.5px; margin-top: 1px; }

  .promise { position: absolute; left: 429px; top: 491px; width: 346px; height: 89px; background: var(--orange);
    color: var(--white); font-size: 24px; line-height: 31px; padding: 16px 0 0 18px; }

  .contact { position: absolute; left: 0; top: 584px; width: 427px; height: 128px; background: var(--slate);
    padding: 25px 0 0 41px; color: var(--white); font-size: 19px; }
  .contact li { list-style: none; display: flex; align-items: center; gap: 12px; height: 32px; }
  .contact svg { width: 22px; height: 22px; flex: none; }

  .social { position: absolute; left: 0; top: 712px; width: 427px; height: 63px; background: var(--navy);
    display: flex; align-items: center; justify-content: center; gap: 10px; padding-left: 20px; }
  .social span { color: var(--white); font-size: 13px; font-weight: 700; }

  .services { position: absolute; left: 429px; top: 584px; width: 346px; height: 191px; background: var(--orange);
    color: var(--white); font-size: 18px; padding: 18px 0 0 18px; }
  .services li { list-style: none; height: 30px; line-height: 30px; }

  .clients { position: absolute; left: 775px; top: 584px; width: 425px; height: 191px; background: var(--mist); padding: 18px 0 0 43px; }
  .clients h2 { font-size: 20px; font-weight: 400; color: #4a4d50; }
  .client-grid { display: grid; grid-template-columns: repeat(4, 94px); row-gap: 32px; margin-top: 34px; }
  .client-grid span { color: var(--client-grey); font-size: 15px; font-weight: 700; }
</style>
</head>
<body>
<div class="ad">
  <div class="top-band"></div>

  <header class="brand">
    <div class="brand-mark"></div>
    <div class="brand-name"><span class="main">Marrowcrest</span><span class="sub">Construction, Inc.</span></div>
  </header>

  <div class="hero" role="img" aria-label="Photo of a crane lifting a concrete tilt-up wall panel on a construction site at sunset"></div>

  <div class="headline">
    <p class="lead">Rising to the challenge since 2003! We love taking on,</p>
    <p class="title">Large scale projects like Tilt Up Construction.</p>
    <p class="value">Our Project Management Team is committed to delivering safe, timely and quality workmanship.</p>
  </div>

  <div class="promise">Quality Service &amp;<br>Expert Workmanship</div>

  <ul class="contact">
    <li><svg viewBox="0 0 24 24" fill="#fff"><path d="M3 9c0-3 4-5 9-5s9 2 9 5v2h-5V9c-1-.6-2.5-1-4-1s-3 .4-4 1v2H3z"/><path d="M6 12h12l2 8H4z"/><circle cx="12" cy="15.5" r="2.3" fill="#55595e"/></svg>916.555.0142</li>
    <li><svg viewBox="0 0 24 24" fill="none" stroke="#fff" stroke-width="2"><rect x="2" y="5" width="20" height="14" rx="2"/><path d="M2 6l10 7 10-7"/></svg>info@marrowcrestbuilding.com</li>
    <li><svg viewBox="0 0 24 24" fill="none" stroke="#fff" stroke-width="1.8"><circle cx="12" cy="12" r="10"/><ellipse cx="12" cy="12" rx="4.5" ry="10"/><path d="M2 12h20M4 7h16M4 17h16"/></svg>marrowcrestbuilding.com</li>
  </ul>

  <nav class="social">
    <span>Fanpage</span><span>Search</span><span>Network</span><span>Posts</span><span>Reviews</span><span>Videos</span>
  </nav>

  <ul class="services">
    <li>Commercial New Construction</li>
    <li>Strip Mall Renovation</li>
    <li>Office Park Builder</li>
    <li>Tilt-Up Construction</li>
    <li>Construction Consulting &amp; Planning</li>
  </ul>

  <section class="clients">
    <h2>Clients Who Trust Us</h2>
    <div class="client-grid">
      <span>Ovenlane</span><span>Pizzafort</span><span>Fieldhouse</span><span>Trail Guild</span>
      <span>Grillwell</span><span>Dressco</span><span>Pantryway</span><span>Northrail</span>
    </div>
  </section>
</div>
</body>
</html>
```